Brookfarrow Osteopathy and dry needling business card

Business card for Brookfarrow Osteopathy and Dry Needling.

Industry/Entity Type

Health

Contact Information for Business Card

I do not have a phone number yet. I also do not have an email address yet. The physical address is: 48 Lower Crane Street Brookfarrow The website is: www.brookfarrowosteosteopathy.example My details are: Dr Martin Pellowe, Osteopath (B.Clin.Sci (Ost) M.Ost BSC ECON (Hons)

Colors
0094D4
00A9DD
6FCCEA
C7EBF8
E9F6FB

Requirements
Must have
• logo on the back
Nice to have
• Maybe a space for me to write an appointment time and date on the card.

```html
<!DOCTYPE html>
<html lang="en">
<head>
<meta charset="utf-8">
<title>Brookfarrow Osteopathy and Dry Needling – Business Card</title>
<link href="https://fonts.googleapis.com/css2?family=Montserrat:wght@600;700&family=Open+Sans:wght@400;600&display=swap" rel="stylesheet">
<style>
  :root {
    --brand-blue: #0094D4;
    --brand-cyan: #00A9DD;
    --brand-sky: #6FCCEA;
    --brand-mist: #C7EBF8;
    --brand-ice: #E9F6FB;
    --accent-orange: #F7941D;
    --text-grey: #5f6368;
    --rule-grey: #9a9a9a;
    --card-white: #ffffff;
    --stage: #e6eaee;
  }
  * { box-sizing: border-box; margin: 0; padding: 0; }
  html, body { width: 1200px; height: 952px; overflow: hidden; }
  body { background: var(--stage); position: relative; font-family: "Open Sans", sans-serif; }

  .card {
    position: absolute;
    left: 250px;
    width: 700px;
    height: 400px;
    background: var(--card-white);
    border-radius: 30px;
    box-shadow: 0 6px 18px rgba(0,0,0,0.12);
    overflow: hidden;
  }
  .card--front { top: 56px; }
  .card--back { top: 496px; }

  /* Brand mark: name with a plain circle */
  .brand {
    display: flex;
    align-items: center;
    gap: 12px;
  }
  .brand__dot {
    width: 34px; height: 34px;
    border-radius: 50%;
    border: 3px solid var(--brand-cyan);
    flex: none;
  }
  .brand__name {
    font-family: "Montserrat", sans-serif;
    font-weight: 600;
    font-size: 15px;
    line-height: 1.3;
    color: var(--brand-blue);
    text-transform: uppercase;
    letter-spacing: 0.06em;
  }

  /* Front */
  .card--front .brand { position: absolute; left: 60px; top: 54px; width: 300px; }
  .person { position: absolute; left: 60px; top: 150px; }
  .person__name {
    font-family: "Montserrat", sans-serif;
    font-weight: 700;
    font-size: 34px;
    color: var(--brand-blue);
    letter-spacing: 0.01em;
  }
  .person__role {
    font-family: "Montserrat", sans-serif;
    font-weight: 600;
    font-size: 20px;
    color: var(--accent-orange);
    margin-top: 2px;
  }
  .person__credentials {
    font-size: 14px;
    color: var(--text-grey);
    margin-top: 4px;
  }
  .contact { position: absolute; left: 60px; top: 292px; list-style: none; }
  .contact__item {
    display: flex; align-items: center; gap: 12px;
    font-size: 14px; color: var(--text-grey);
    margin-bottom: 10px;
  }
  .contact__icon {
    width: 22px; height: 22px;
    border-radius: 5px;
    background: var(--accent-orange);
    display: flex; align-items: center; justify-content: center;
    flex: none;
  }

  /* Back */
  .card--back .brand { position: absolute; right: 60px; top: 60px; width: 280px; }
  .appointment__title {
    position: absolute; left: 290px; top: 170px;
    font-family: "Montserrat", sans-serif;
    font-weight: 600;
    font-size: 30px;
    color: var(--accent-orange);
    letter-spacing: 0.02em;
  }
  .appointment__field {
    position: absolute; left: 60px;
    display: flex; align-items: flex-end; gap: 8px;
    font-family: "Montserrat", sans-serif;
    font-weight: 600;
    font-size: 17px;
    color: var(--brand-blue);
  }
  .appointment__field--date { top: 250px; width: 320px; }
  .appointment__field--time { top: 250px; left: 400px; width: 240px; }
  .appointment__line {
    flex: 1;
    border-bottom: 2px dashed var(--rule-grey);
    margin-bottom: 4px;
  }
</style>
</head>
<body>

<section class="card card--front" aria-label="Business card front">
  <div class="brand">
    <span class="brand__dot"></span>
    <span class="brand__name">Brookfarrow Osteopathy &amp; Dry Needling</span>
  </div>

  <div class="person">
    <h1 class="person__name">Dr Martin Pellowe</h1>
    <p class="person__role">Osteopath</p>
    <p class="person__credentials">(B.Clin.Sci (Ost) M.Ost BSC ECON (Hons)</p>
  </div>

  <ul class="contact">
    <li class="contact__item">
      <span class="contact__icon">
        <svg width="12" height="14" viewBox="0 0 12 14" aria-hidden="true"><path d="M6 0.8a4.6 4.6 0 0 0-4.6 4.6C1.4 8.8 6 13.2 6 13.2s4.6-4.4 4.6-7.8A4.6 4.6 0 0 0 6 0.8z" fill="none" stroke="#fff" stroke-width="1.6"/><circle cx="6" cy="5.4" r="1.6" fill="#fff"/></svg>
      </span>
      48 Lower Crane Street Brookfarrow
    </li>
    <li class="contact__item">
      <span class="contact__icon">
        <svg width="14" height="14" viewBox="0 0 14 14" aria-hidden="true"><circle cx="7" cy="7" r="5.8" fill="none" stroke="#fff" stroke-width="1.4"/><ellipse cx="7" cy="7" rx="2.6" ry="5.8" fill="none" stroke="#fff" stroke-width="1.2"/><line x1="1.2" y1="7" x2="12.8" y2="7" stroke="#fff" stroke-width="1.2"/></svg>
      </span>
      www.brookfarrowosteosteopathy.example
    </li>
  </ul>
</section>

<section class="card card--back" aria-label="Business card back">
  <div class="brand">
    <span class="brand__dot"></span>
    <span class="brand__name">Brookfarrow Osteopathy &amp; Dry Needling</span>
  </div>

  <h2 class="appointment__title">AN APPOINTMENT</h2>

  <div class="appointment__field appointment__field--date">
    <span>Date</span><span class="appointment__line"></span>
  </div>
  <div class="appointment__field appointment__field--time">
    <span>Time</span><span class="appointment__line"></span>
  </div>
</section>

</body>
</html>
```